Brightmark Power website design

Electrical contractor in Perth that services the domestic and commercial markets. our services include but not limited to:

New Home Installations and Design
Commercial Shop Fit Outs
Rewires
Renovations
Switchboard Upgrades
Kitchen and Bathroom Renovations
RCD'S (Safety Switches)
Smoke Alarms
Power points
Security Lighting
Energy Efficient LED Lighting Designs
Garden Lighting
Downlights
General Electrical Maintenance
TV and Phone Points
Home Theatre Installs
Safety Certificates
24hr Call out service
Electric Hot Water Units
Credit cards accepted

www.sociabook.example/brightmarkpower

Contractor

5+ page

Sans Serif

acd037
fbee3e

• contact page, services page, about us, careers page, somewhere I can put some testimonials, somewhere potential clients can book our services online, on the homepage somewhere showing that we can provide 24/7 emergency service
• icon stating that we accept all major credit cards

```html
<!DOCTYPE html>
<html lang="en">
<head>
<meta charset="utf-8">
<title>Brightmark Power</title>
<link href="https://fonts.googleapis.com/css2?family=Arimo:wght@400;700&family=Lato:wght@400;700;900&display=swap" rel="stylesheet">
<style>
:root{
  --lime:#acd037;
  --lime-dark:#93b52a;
  --yellow:#fbee3e;
  --navy:#1d2b55;
  --ink:#2d2d2d;
  --body:#444;
  --muted:#888;
  --page:#f7f7f5;
  --rule:#dcdcdc;
  --footer:#2a2828;
  --footer-text:#b5b5b5;
  --white:#fff;
}
*{margin:0;padding:0;box-sizing:border-box}
html,body{width:1189px;height:1200px;overflow:hidden}
body{position:relative;background:var(--page);font-family:'Arimo',Arial,sans-serif;color:var(--body)}
.abs{position:absolute}

/* header */
.topbar{left:0;top:0;width:1189px;height:59px;background:var(--lime)}
.emergency{right:22px;top:6px;color:var(--white);font-weight:700;font-size:12px;display:flex;align-items:center;gap:6px;letter-spacing:.2px}
.brand{left:243px;top:0;width:213px;height:72px;background:linear-gradient(#fff,#ececec);border-radius:0 0 10px 10px;box-shadow:0 2px 5px rgba(0,0,0,.35);display:flex;align-items:center;justify-content:center;gap:10px}
.brand-name{font-family:'Arimo',Arial,sans-serif;font-weight:700;font-size:19px;color:var(--lime-dark);line-height:1}
.brand-mark{width:14px;height:14px;border-radius:50%;background:var(--navy)}
.nav{left:634px;top:24px;display:flex;height:35px}
.nav a{color:var(--white);text-decoration:none;font-size:11px;font-weight:400;padding:0 15px;line-height:35px;letter-spacing:.2px}
.nav a.active{background:var(--white);color:var(--lime-dark)}

/* hero */
.hero{left:0;top:59px;width:1189px;height:408px;background:radial-gradient(ellipse at 50% 45%,#3e4fa8 0%,#2c3570 22%,#3a3530 48%,#1f1c19 100%)}
.tagline{right:256px;top:290px;text-align:right;color:var(--white);font-family:'Lato',Arial,sans-serif;text-shadow:0 1px 3px rgba(0,0,0,.4)}
.tagline .small{font-size:22px;letter-spacing:6px;font-weight:400;line-height:26px}
.tagline .big{font-size:53px;font-weight:700;letter-spacing:1px;line-height:52px}
.learn{left:843px;top:367px;width:86px;height:19px;background:var(--lime);color:var(--white);font-size:9px;font-weight:700;display:flex;align-items:center;justify-content:center;gap:6px}
.dots{left:258px;top:445px;display:flex;gap:5px}
.dots span{width:10px;height:10px;border-radius:50%;background:var(--white)}
.dots span:first-child{background:transparent;border:2px solid var(--white)}

/* featured */
.section-title{font-size:13.5px;font-weight:700;color:var(--ink);letter-spacing:.2px}
.btn{background:var(--lime);color:var(--white);font-size:8px;font-weight:700;display:flex;align-items:center;justify-content:center;height:17px;white-space:nowrap}
.btn-projects{font-size:6.8px;padding:0 4px;letter-spacing:0}
.work{width:153px}
.work .thumb{height:106px}
.work h3{font-size:10.5px;color:var(--ink);margin-top:19px}
.work p{font-size:8.4px;line-height:13px;margin-top:11px;text-align:justify}
.work .btn{width:36px;margin-top:15px}
.rule{left:255px;top:700px;width:674px;height:1px;background:var(--rule)}

/* about / clients */
.about{left:255px;top:755px;width:340px}
.about-img{float:left;width:129px;height:72px;margin:0 12px 4px 0;background:linear-gradient(#dfe6ee,#f2f2f2 60%,#b9bcc0)}
.about-text{font-size:8.4px;line-height:13px;text-align:justify}
.clients{left:645px;top:762px;display:flex;gap:26px;align-items:center}
.client{display:flex;align-items:center;gap:5px;font-size:13px;font-weight:700;color:var(--lime-dark)}
.client i{width:10px;height:10px;background:var(--lime-dark);border-radius:50%;display:block}
.avatar{left:647px;top:842px;width:41px;height:41px;border-radius:50%;background:linear-gradient(#d8b39a,#7a5646);border:2px solid #eee}
.quote-who{left:636px;top:890px;width:64px;text-align:center;font-size:8.5px;line-height:11px}
.quote-who b{color:var(--lime-dark)}
.quote-mark{left:708px;top:866px;font-family:Georgia,serif;font-size:26px;color:#bbb}

/* footer */
.footer{left:0;top:956px;width:1189px;height:244px;background:var(--footer)}
.f-title{color:var(--white);font-size:10.5px;font-weight:700;letter-spacing:.3px}
.f-text{color:var(--footer-text);font-size:9.5px;line-height:13px}
.f-row{display:flex;gap:8px;align-items:flex-start;white-space:nowrap}
.f-row b{color:var(--white);font-weight:400}
.f-link{color:var(--yellow);text-decoration:underline}
.social{display:flex;gap:7px}
.social span{width:15px;height:15px;border-radius:50%;background:#9a9a9a}
.social span.on{background:#3db4e5}
.news{display:flex;gap:12px;width:208px;padding-bottom:10px;border-bottom:1px solid #454343;margin-bottom:12px}
.news-thumb{width:37px;height:30px;flex:none;background:linear-gradient(#c9a882,#6b4e33)}
.news-date{color:#6f6d6d}
.email{left:724px;top:1056px;width:205px;height:27px;display:flex}
.email span{flex:1;background:#8a8a8a;color:#222;font-size:9px;padding-left:11px;line-height:27px}
.email b{width:29px;background:var(--lime);display:flex;align-items:center;justify-content:center}
.pay{left:727px;top:1116px;display:flex;gap:16px;align-items:center}
.pay span{color:var(--white);font-weight:700;font-size:16px}
.copyright{left:0;top:1169px;width:1189px;height:31px;border-top:1px solid #3d3b3b;text-align:center;color:var(--footer-text);font-size:8.5px;line-height:28px}
.copyright b{color:var(--white)}
</style>
</head>
<body>

<header>
  <div class="abs topbar"></div>
  <div class="abs emergency">
    <svg width="13" height="13" viewBox="0 0 13 13"><circle cx="6.5" cy="6.5" r="6.5" fill="#fff"/><path d="M3.5 6.7l2 2 4-4.2" stroke="#acd037" stroke-width="1.8" fill="none"/></svg>
    24/7 EMERGENCY SERVICE
  </div>
  <div class="abs brand"><span class="brand-mark"></span><span class="brand-name">Brightmark Power</span></div>
  <nav class="abs nav">
    <a class="active">HOME</a><a>ABOUT US</a><a>SERVICES</a><a>CONTACT US</a><a>CAREER</a>
  </nav>
</header>

<section>
  <div class="abs hero" role="img" aria-label="Photo of a studio light tent with tripod and two lamps"></div>
  <div class="abs tagline"><div class="small">YOUR TAGLINE</div><div class="big">IS HERE</div></div>
  <div class="abs learn">LEARN MORE
    <svg width="10" height="10" viewBox="0 0 10 10"><circle cx="5" cy="5" r="5" fill="#fff"/><path d="M4 2.8l2.3 2.2L4 7.2" stroke="#acd037" stroke-width="1.4" fill="none"/></svg>
  </div>
  <div class="abs dots"><span></span><span></span><span></span><span></span></div>
</section>

<section>
  <h2 class="abs section-title" style="left:257px;top:490px">FEATURED WORKS</h2>
  <div class="abs btn btn-projects" style="left:257px;top:512px;min-width:87px">CHECK OUT PROJECTS</div>

  <article class="abs work" style="left:441px;top:423px">
    <div class="thumb" role="img" aria-label="Photo of a modern office building" style="background:linear-gradient(#cfd3d6,#8c9094 60%,#5d7a3c)"></div>
    <h3>INNOVATION SQUARE</h3>
    <p>Lid est laborum dolo rumes fugats untras. Etharums ser quidem rerum facilis dolores nemis omnis fugats vitaes nemo minima rerums unsers sadips amets.. Sed ut perspiciatis unde omnis iste natus error sit voluptatem...</p>
    <div class="btn">MORE</div>
  </article>
  <article class="abs work" style="left:609px;top:423px">
    <div class="thumb" role="img" aria-label="Photo of a city skyline at night" style="background:linear-gradient(#3a2f7a,#5a56b8 55%,#1b1b3a)"></div>
    <h3>INNOVATION SQUARE</h3>
    <p>Lid est laborum dolo rumes fugats untras. Etharums ser quidem rerum facilis dolores nemis omnis fugats vitaes nemo minima rerums unsers sadips amets.. Sed ut perspiciatis unde omnis iste natus error sit voluptatem...</p>
    <div class="btn">MORE</div>
  </article>
  <article class="abs work" style="left:777px;top:423px">
    <div class="thumb" role="img" aria-label="Photo of a power pylon in a green field" style="background:linear-gradient(#2f73d6,#8cc4ef 55%,#6fae2f 75%,#4e8a22)"></div>
    <h3>INNOVATION SQUARE</h3>
    <p>Lid est laborum dolo rumes fugats untras. Etharums ser quidem rerum facilis dolores nemis omnis fugats vitaes nemo minima rerums unsers sadips amets.. Sed ut perspiciatis unde omnis iste natus error sit voluptatem...</p>
    <div class="btn">MORE</div>
  </article>
  <div class="abs rule"></div>
</section>

<section>
  <h2 class="abs section-title" style="left:255px;top:721px">WHAT WE DO</h2>
  <div class="abs about">
    <div class="about-img" role="img" aria-label="Photo of a business team standing on a bright floor"></div>
    <p class="about-text">Lid est laborum dolo rumes fugats untras. Etharums ser quidem rerum facilis dolores nemis omnis fugats vitaes nemo minima rerums unsers sadips amets.. Sed ut perspiciatis unde omnis iste natus error sit voluptatem accusantium doloremque laudantium, totam rem aperiam, eaque ipsa quae ab illo inventore veritatis et quasi architecto beatae vitae dicta sunt explicabo. Nemo enim ipsam voluptatem quia voluptas sit aspernatur aut odit aut fugit.</p>
    <div class="btn" style="width:55px;margin-top:14px">READ MORE</div>
  </div>

  <h2 class="abs section-title" style="left:645px;top:721px">OUR CLIENTS</h2>
  <div class="abs clients">
    <span class="client"><i></i>Orbit</span>
    <span class="client">Tandem</span>
    <span class="client">Kestrel</span>
    <span class="client">Delvo</span>
  </div>

  <div class="abs avatar" role="img" aria-label="Portrait of the reviewer"></div>
  <div class="abs quote-who"><b>Dana Hale</b><br>Norvale Inc</div>
  <h3 class="abs section-title" style="left:708px;top:843px;font-size:10.5px;color:var(--navy)">WHAT PEOPLE SAY ABOUT US</h3>
  <div class="abs quote-mark">&ldquo;</div>
  <p class="abs about-text" style="left:708px;top:873px;width:222px;text-indent:20px">Nemo enim ipsam voluptatem quia voluptas sit aspernatur aut odit aut fugit, sed quia consequuntur magni dolores eos qui ratione vol sequi nesciunt..</p>
</section>

<footer>
  <div class="abs footer"></div>

  <h4 class="abs f-title" style="left:257px;top:982px">CONTACT US</h4>
  <div class="abs f-text" style="left:257px;top:1009px;width:200px">
    <div class="f-row"><svg width="11" height="10" viewBox="0 0 11 10"><path d="M5.5 0L0 5h1.5v5h3V7h2v3h3V5H11z" fill="#8a8a8a"/></svg><div><b>Address:</b> Eastvale<br>Perth, Western Australia</div></div>
    <div class="f-row" style="margin-top:5px"><svg width="11" height="11" viewBox="0 0 11 11"><path d="M2 0l2 3-1 1.2c.7 1.5 1.8 2.6 3.3 3.3L7.5 6.5l3 2-1 2.3C4.8 10.5.5 6.2 0 1.5z" fill="#8a8a8a"/></svg><div><b>Mobile:</b> +61 400 555 123</div></div>
    <div class="f-row" style="margin-top:5px"><svg width="11" height="9" viewBox="0 0 11 9"><rect width="11" height="9" fill="#8a8a8a"/><path d="M0 0l5.5 5L11 0" stroke="#2a2828" fill="none"/></svg><div><b>Email:</b> <span class="f-link">info@brightmarkpower.example</span></div></div>
  </div>
  <div class="abs social" style="left:257px;top:1083px"><span></span><span></span><span></span><span class="on"></span><span></span><span></span></div>

  <h4 class="abs f-title" style="left:477px;top:982px">LATEST NEWS</h4>
  <div class="abs f-text" style="left:477px;top:1014px">
    <div class="news"><div class="news-thumb" role="img" aria-label="Photo of a living room"></div><div>Mauris ut mauris sit amet nisi lobortis interdum.<br><span class="news-date">October 22, 2020</span></div></div>
    <div class="news"><div class="news-thumb" role="img" aria-label="Photo of a bedroom"></div><div>Mauris ut mauris sit amet nisi<br><span class="news-date">October 22, 2020</span></div></div>
    <div class="news" style="border:0"><div class="news-thumb" role="img" aria-label="Photo of a lounge"></div><div>Mauris ut mauris sit amet nisi<br><span class="news-date">October 22, 2020</span></div></div>
  </div>

  <h4 class="abs f-title" style="left:724px;top:982px">NEWSLETTER</h4>
  <p class="abs f-text" style="left:724px;top:1009px;width:210px">Vestibulum sem nulla, euismod ac facilisis in, condimentum adipiscing urna. Ut at diam mi. Vivamus sed ligula odio.</p>
  <div class="abs email"><span>Enter your Email...</span><b><svg width="12" height="12" viewBox="0 0 12 12"><path d="M0 5l12-5-5 12-1.5-5.5z" fill="#fff"/></svg></b></div>
  <div class="abs pay"><span>PayNest</span><span>CardOne</span><span>Vantis</span></div>

  <div class="abs copyright"><b>BRIGHTMARK POWER</b> &copy; COPYRIGHT 2014</div>
</footer>

</body>
</html>
```